Business broker needs designs for business card, letterhead and email signature

I require the following items:
- business cards
- letterhead
- email signature

My company is a Business Broker company that specialises in business sales across various industries. The company has branches in four areas and each area has its own logo and website. Initially for the submission I am happy to inspect 1 design and 1 layout for quillharborgroup but the winner will need to complete a design for each area.

The four areas are:
1. quillharborgroup
2. tealridgefuelsales
3. orbvalechainsales
4. pondgrovegrocerdeals

I would like one design for each of the above items for each area. In each design, there should be one prominent logo and then the remaining three should also be included, for eg, the letterhead for the quillharborgrp area would have the quillharborgrp logo featuring prominently, somewhere at the top perhaps and the logos of the other three areas would be smaller and perhaps at the bottom, down the side, etc.

For the business cards, one prominent logo should feature on one side with the remaining three logos on the reverse.

The overall objective is for each item to look like it belongs to one family . I need all the source files as I may add new industries moving forward.

Target Market(s)

My company targets business minded people looking to increase wealth,. make an investment or migrate to Australia. People who busy and are looking for efficient and professional service in securing their next business venture.

Industry/Entity Type

Business

Font styles to use
Serif
Sans Serif

Requirements
Must have
• I want something professional and corporate looking, not something cartoony or playful. I am happy for you to be creative.

```html
<!DOCTYPE html>
<html lang="en">
<head>
<meta charset="utf-8">
<title>pondgrovegrocerdeals – Business Card</title>
<link rel="stylesheet" href="https://fonts.googleapis.com/css2?family=Jost:wght@400;600;700&display=swap">
<style>
  :root {
    --ink: #3a3f47;
    --charcoal: #2f353d;
    --green: #8cc63f;
    --paper: #ffffff;
    --red: #d7262e;
    --orange: #f29a1f;
    --teal: #1f8f86;
  }
  html, body {
    margin: 0;
    padding: 0;
    overflow: hidden;
    background: var(--paper);
  }
  .card {
    position: relative;
    width: 1200px;
    height: 686px;
    background: var(--paper);
    overflow: hidden;
    font-family: "Jost", "Century Gothic", sans-serif;
    color: var(--ink);
  }
  .brand {
    position: absolute;
    top: 72px;
    left: 0;
    width: 100%;
    display: flex;
    justify-content: center;
    align-items: center;
    gap: 22px;
  }
  .brand__mark {
    width: 66px;
    height: 66px;
    background: var(--green);
  }
  .brand__name {
    font-size: 72px;
    font-weight: 700;
    letter-spacing: -1px;
    color: var(--ink);
    line-height: 1;
  }
  .divider {
    position: absolute;
    left: 609px;
    top: 222px;
    width: 3px;
    height: 280px;
    background: linear-gradient(to bottom, rgba(58,63,71,0), rgba(58,63,71,0.55) 20%, rgba(58,63,71,0.55) 80%, rgba(58,63,71,0));
  }
  .person {
    position: absolute;
    left: 234px;
    top: 330px;
  }
  .person__name {
    font-size: 40px;
    font-weight: 700;
    line-height: 1.1;
  }
  .person__role {
    font-size: 30px;
    font-weight: 400;
    line-height: 1.3;
  }
  .contact {
    position: absolute;
    left: 673px;
    top: 292px;
    font-size: 31px;
    line-height: 38px;
    font-weight: 400;
  }
  .contact p { margin: 0; }
  .family {
    position: absolute;
    top: 583px;
    left: 46px;
    display: flex;
    gap: 40px;
    align-items: center;
  }
  .family__item {
    display: flex;
    align-items: center;
    gap: 8px;
    font-size: 22px;
    font-weight: 700;
    color: var(--ink);
  }
  .family__mark {
    width: 22px;
    height: 22px;
  }
  .family__mark--red { background: var(--red); }
  .family__mark--orange { background: var(--orange); }
  .family__mark--teal { background: var(--teal); }
  .footer-band {
    position: absolute;
    left: 0;
    bottom: 0;
    width: 100%;
    height: 52px;
    background: var(--charcoal);
  }
  .footer-band__web {
    position: absolute;
    left: 0;
    width: 1200px;
    bottom: 8px;
    text-align: center;
    font-size: 29px;
    color: var(--paper);
  }
  .corner {
    position: absolute;
    left: 0;
    top: 0;
  }
</style>
</head>
<body>
  <div class="card">
    <div class="brand">
      <div class="brand__mark"></div>
      <div class="brand__name">pondgrovegrocerdeals</div>
    </div>

    <div class="divider"></div>

    <div class="person">
      <div class="person__name">Name Business</div>
      <div class="person__role">Manager Company</div>
    </div>

    <div class="contact">
      <p>Kestrel 18 20451</p>
      <p>P.O Box 3872</p>
      <p>info@quillharborgroup.com</p>
      <p>+000 000 0 000</p>
    </div>

    <div class="family">
      <div class="family__item"><span class="family__mark family__mark--red"></span>quillharborgroup</div>
      <div class="family__item"><span class="family__mark family__mark--orange"></span>orbvalechainsales</div>
      <div class="family__item"><span class="family__mark family__mark--teal"></span>tealridgefuelsales</div>
    </div>

    <div class="footer-band"></div>

    <svg class="corner" width="1200" height="686" viewBox="0 0 1200 686" aria-hidden="true">
      <polygon points="1060,600 1200,462 1200,686 1060,686" fill="var(--charcoal)"/>
      <polygon points="975,686 1135,548 1200,612 1200,686" fill="var(--green)"/>
    </svg>

    <div class="footer-band__web">www.quillharborgroup.com</div>
  </div>
</body>
</html>
```